Downloadable PDF "Brochure?"

We have a Free download we will provide in exchange for an email address on our new Trailmark website. The website at www.venturetrailmark-example.com is in development and will look nothing like what it currently does, but you can go there and get a sense of what Trailmark is from the text on the website. (see the attached image 'site design' for the new redesigned website for aesthetics).

We are looking for a nice design for the document, that will represent the mostly text document well. We are not actually looking to print these at a printer so they don't have to be print ready. I went ahead and included the logo and colors and fonts file again just for reference.

Target Market(s)

Business Owners / Decision Makers

Requirements
Must have
• See attached document 'trailmark freebie' for text to be utilized in the finished deliverable.
• See the attached image 'Site Design' for the website aesthetic.

```html
<!DOCTYPE html>
<html lang="en">
<head>
<meta charset="utf-8">
<title>Trailmark – 10 Questions to Choose the Best Technology Advisor</title>
<link rel="stylesheet" href="https://fonts.googleapis.com/css2?family=Cinzel:wght@700&family=Open+Sans:wght@300;400;700&display=swap">
<style>
  :root{
    --stage:#6f6f6f;
    --stage-light:#8a8a8a;
    --paper:#f2f2f2;
    --paper-edge:#e6e6e6;
    --sky:#d6ecf8;
    --copper:#c2773f;
    --copper-text:#b9612a;
    --slate:#36474f;
    --ink:#2a2a2a;
    --body:#6a6a6a;
    --white:#ffffff;
  }
  *{margin:0;padding:0;box-sizing:border-box}
  html,body{width:1200px;height:2190px;overflow:hidden}
  body{
    background:radial-gradient(ellipse at 50% 40%,var(--stage-light),var(--stage) 75%);
    font-family:"Open Sans",Arial,sans-serif;
    position:relative;
  }
  .page{
    position:absolute;width:511px;height:660px;
    background:linear-gradient(135deg,var(--paper),var(--paper-edge));
    box-shadow:0 2px 10px rgba(0,0,0,.35);
    overflow:hidden;
  }
  .col-left{left:61px}
  .col-right{left:625px}
  .row-1{top:80px}
  .row-2{top:771px}
  .row-3{top:1463px}

  .page-body{padding:52px 62px 0 56px}
  .q{
    color:var(--copper-text);font-weight:700;font-size:14.5px;line-height:1.38;letter-spacing:.2px;
  }
  .rule{
    display:block;width:22px;height:3px;background:var(--slate);margin:8px 0 11px;
  }
  .copy{
    font-size:8.6px;line-height:1.5;color:var(--body);margin-bottom:24px;
  }
  .page-foot{position:absolute;left:0;right:0;bottom:22px;height:25px}
  .foot-url{
    position:absolute;left:0;top:0;height:25px;width:215px;background:var(--slate);
    color:var(--white);font-size:8.5px;line-height:25px;padding-left:52px;
  }
  .foot-num{
    position:absolute;right:20px;top:0;width:25px;height:25px;background:var(--copper);
    color:var(--white);font-size:8.5px;line-height:25px;text-align:center;
  }

  /* cover */
  .cover{background:var(--white)}
  .cover-sky{position:absolute;left:0;top:0;width:100%;height:496px;background:var(--sky)}
  .cover-title{
    position:absolute;top:64px;left:0;width:100%;text-align:center;
    font-family:"Cinzel",Georgia,serif;font-weight:700;font-size:26px;line-height:1.25;
    color:#111;letter-spacing:.5px;
  }
  .cover-sub{
    position:absolute;top:146px;left:0;width:100%;text-align:center;font-size:10px;color:#222;
  }
  .cover-art{
    position:absolute;left:48px;top:190px;width:415px;height:190px;border-radius:4px;
    background:radial-gradient(ellipse at center,#c3d7e3,#d6ecf8 70%);
  }
  .brand-dot{
    position:absolute;left:215px;top:430px;width:82px;height:82px;border-radius:50%;
    background:var(--white);
  }
  .brand-name{
    position:absolute;top:540px;left:0;width:100%;text-align:center;
    font-family:"Open Sans",Arial,sans-serif;font-weight:700;font-size:24px;color:var(--slate);letter-spacing:.5px;
  }
  .cover-foot{
    position:absolute;left:0;bottom:0;width:100%;height:40px;background:var(--copper);
    color:var(--white);font-size:12px;line-height:40px;text-align:center;
  }
  .cover-foot b{font-weight:700}

  /* intro page */
  .title-light{font-weight:300;font-size:22px;color:var(--ink);letter-spacing:.3px;line-height:1.2}
  .title-bold{font-weight:700;font-size:22px;color:var(--copper-text);letter-spacing:.3px;line-height:1.2;margin-bottom:20px}
  .q-stack{margin-top:40px}
  .q-stack .q{margin-bottom:10px}

  .art{position:absolute}
  .crowd{left:250px;top:450px;width:175px;height:130px;
    background:linear-gradient(160deg,rgba(180,110,80,.35),rgba(120,140,160,.25));border-radius:4px}
  .advisor-scene{left:0;top:285px;width:100%;height:215px;
    background:radial-gradient(ellipse at 50% 55%,#5aa9e0,#c9dfee 55%,rgba(242,242,242,0) 80%)}

  .contact-head{position:absolute;top:520px;left:56px;font-size:13px;font-weight:400;color:var(--ink)}
  .contact-head b{color:var(--copper-text);font-weight:700}
  .contact-addr{position:absolute;top:557px;left:56px;font-size:8.5px;line-height:1.5;color:var(--ink)}
  .contact-right{position:absolute;top:557px;right:52px;font-size:8.5px;line-height:2.3;color:var(--ink);text-align:right}
</style>
</head>
<body>

<!-- Cover -->
<section class="page cover col-left row-1">
  <div class="cover-sky"></div>
  <h1 class="cover-title">TECHNOLOGY ADVISORS<br>THAT "GET" BUSINESS.</h1>
  <p class="cover-sub">We help you leverage technology to create a competitive advantage.</p>
  <div class="cover-art" role="img" aria-label="Line-art doodles of business and technology icons around a central 'business' note with a rising bar chart"></div>
  <div class="brand-dot"></div>
  <div class="brand-name">Trailmark</div>
  <div class="cover-foot">www.<b>VentureTrailmark-example</b>.com</div>
</section>

<!-- Page 01 -->
<section class="page col-right row-1">
  <div class="page-body">
    <h2 class="title-light">10 QUESTIONS TO CHOOSE</h2>
    <h2 class="title-bold">THE BEST TECHNOLOGY ADVISOR</h2>
    <p class="copy">When you choose a technology advisor whether it be a Managed Service Provider, fractional CIO or a full-time CIO you need to make sure that they understand business just as much as they understand technology. Some of the biggest complaints about the IT department are that they just don't "Get it". The questions below should help you determine whether or not they have a technology mindset or a business mindset.</p>
    <div class="q-stack">
      <p class="q">What is scalability?</p>
      <p class="q">How important is it from a technology perspective on a scale of 1-&gt;10 with 10 being the highest?</p>
      <p class="q">What all does scalability impact?</p>
    </div>
    <span class="rule"></span>
    <p class="copy" style="margin-top:22px">This question is designed to get a reading on the person's mindset. A typical technology-minded response would be something describing the ability of systems or software to scale by adding additional resources. When working from a business point of view, however, you want to see it defined as the ability for the organization to support increased volume without sacrificing margins. The importance of this concept cannot be overstated and should be a 9 or 10 in terms of ranking. Regarding impact, you want to see not just an understanding of having to spend money two or three times for a different solution to the same problem, but an acknowledgment of the 'total' cost, including adoption fatigue, the opportunity cost of change, and the competitive disadvantage it creates. For concepts of business scalability refer to 'Growing Wide' by Vera Hollis.</p>
  </div>
  <div class="page-foot"><div class="foot-url">www.VentureTrailmark-example.com</div><div class="foot-num">01</div></div>
</section>

<!-- Page 02 -->
<section class="page col-left row-2">
  <div class="page-body">
    <p class="q">Provide an example where you solved a problem without the use of technology.</p>
    <span class="rule"></span>
    <p class="copy">Often technology-minded individuals become so wrapped up in the solutions themselves they fail to realize a policy or process change is far more effective and simple than making changes to existing or introducing new technology. Asking for a specific example here should demonstrate the ability to think from a business mindset. For specific examples reference 'The Open Ledger' by Lane, Orrin, and Pell.</p>
    <p class="q">How do you go about prioritizing solutions in order of importance for implementation / adoption?</p>
    <span class="rule"></span>
    <p class="copy">Answers here should include reference to some form of discovery process or a thorough evaluation at the operations level. One of the key skill sets for someone approaching technology from a business point of view is mapping solutions and their respective importance to business outcomes and (often more importantly) eliminating bottlenecks while respecting that some implementations must necessarily come before others to be viable. For reference on the Theory of Constraints see 'The Throughput' by Avram Kessler.</p>
    <p class="q">What is Information Technology Debt?</p>
    <span class="rule"></span>
    <p class="copy">Stated simply, 'IT Debt' is a measurement of the out-of-date, incomplete or yet-to-be-defined technology changes. Debt occurs for a number of reasons, including lack of qualified personnel to implement the needed solutions (or recognize the problem in the first place); historical spending haunting the organization "we spent money on something like this before and look what it got us"; fire-fighting (addressing issues purely reactively in a downward spiral leaving no time for fixing the real underlying problem); or most commonly, the budget being already allocated to other company endeavors that seem immediately more pressing. By recognizing what IT Debt is, the individual demonstrates an acknowledgment of how impactful it can be when neglected and not brought to the forefront of business planning sessions.</p>
  </div>
  <div class="page-foot"><div class="foot-url">www.VentureTrailmark-example.com</div><div class="foot-num">02</div></div>
</section>

<!-- Page 03 -->
<section class="page col-right row-2">
  <div class="page-body">
    <p class="q">Provide an example where you argued against implementing a technology solution and why.</p>
    <span class="rule"></span>
    <p class="copy">Despite it being seemingly obvious, using 'outside of budget' is not a good answer. Business-minded technology advisors should be intimately aware of how well a proposed solution will integrate into the existing company ecosystem (software tools already present, workflow, and processes), if it drives the company toward reducing/eliminating a bottleneck (and thereby creates more leverage), and if it fits the company's culture. If any of these are a no, the solution should be carefully examined for what it really offers the organization. If yes, the budget should be evaluated as a cost-benefit analysis, not a flat number 'not to exceed'.</p>
    <p class="q">What is your ideal method for maintaining technology alignment for the company?</p>
    <span class="rule"></span>
    <p class="copy">You want to see a specific process envisioned here. At the very least a recommendation to be involved in business planning meetings or retreats, and ideally a standing technology focused meeting with leadership present should be argued for. For technology to be truly in alignment, it must fit the needs of the organization, not the other way around. This needs to come from the top level, and it means a representative must be present in critical business strategy meetings to understand where the company is headed, what operational constraints they are encountering, and what their short-term goals are. For an outline of how this model has been the underlying key to success for several well-known companies reference 'Steady to Strong' by Jon Corwell.</p>
  </div>
  <div class="art crowd" role="img" aria-label="Illustration of a crowd of small people forming a rising diagonal arrow"></div>
  <div class="page-foot"><div class="foot-url">www.VentureTrailmark-example.com</div><div class="foot-num">03</div></div>
</section>

<!-- Page 04 -->
<section class="page col-left row-3">
  <div class="page-body">
    <p class="q">How do you plan on measuring and monitoring the adoption success of a solution or project?</p>
    <span class="rule"></span>
    <p class="copy">Technically minded individuals often look at the point of 'it's up and running and it all works', as where their responsibilities end. Someone with a business mindset should demonstrate that evaluating how well the solution has been adopted into the day to day workflow, and to what degree the solution has increased leverage or operational transparency are the true critical indicators of success. There should be a specific process of follow-up after implementation to flag adoption or workflow issues due to problems such as inadequate training, unforeseen incompatibilities (whether they be process or technology related), or simply resistance to change. These findings can then be brought back to leadership to evaluate how best to improve successful adoption going forward.</p>
    <p class="q">Provide an example where you had to balance customer and employee technology experience with security and compliance.</p>
    <span class="rule"></span>
    <p class="copy">A critical role fulfilled by a technology advisor is being able to balance maintaining compliance and sound security practices with as painless of a technology experience as possible. They should be able to weigh the critical importance of protecting the organization from the negative public relations and liability of a security flaw while respecting a solution must be usable to be useful. Look for an example that demonstrates an understanding of both sides and strikes a balance without going to an extreme in either direction.</p>
    <p class="q">What would you do first, if you were selected as our advisor? Can you give me details on what your discovery or on-boarding process includes?</p>
    <span class="rule"></span>
    <p class="copy">You are looking to make sure that they don't stop at the technology. There should be a higher focus on understanding what the company processes are and how the people inside the organization get work done. If they focus only on network, security, and disaster recovery assessments then they do not have a business mindset.</p>
  </div>
  <div class="page-foot"><div class="foot-url">www.VentureTrailmark-example.com</div><div class="foot-num">04</div></div>
</section>

<!-- Page 05 -->
<section class="page col-right row-3">
  <div class="page-body">
    <p class="q">Can you give me an example of a time you gave a suggestion for a solution and it was not taken? Describe the solution and why it was important to the organization.<br>And why do you think they didn't implement it?</p>
    <span class="rule"></span>
    <p class="copy">When they describe why they think the solution was important do they simply talk about risk reduction or uptime improvements without tying them back to an organizational goal or bottleneck. Being able to demonstrate actual business value is a critical skill for a technology advisor. For reference on technical excellence in service of business objectives rather than blindly servicing requirements see 'A Voice in The Room' by Mark Stroud.</p>
  </div>
  <div class="art advisor-scene" role="img" aria-label="Illustration of a businessman with a briefcase and magnifying glass standing on a globe above a rising red line chart"></div>
  <h3 class="contact-head">CONTACT <b>US</b></h3>
  <p class="contact-addr">4120 Meridian Parkway South, Suite 200<br>Brookfield, TX 75010</p>
  <p class="contact-right">(555) 010-0142<br>hello@venturetrailmark-example.com</p>
  <div class="page-foot"><div class="foot-url">www.VentureTrailmark-example.com</div><div class="foot-num">05</div></div>
</section>

</body>
</html>
```